Navigate the Underground Car Park to 7K3R Vet Clinic

Eye-catching signage for Underground Carpark.
We want to help new Clients, or those with bad senses of direction, to the correct Lift Lobby.
We want to be able to say 'Just follow the signs'.

It can be confusing and many other business have utilised some of the pillars in the carpark to guide their customers to the right place.

People don't want to walk far with sick animals so it is important they get to the right Lift Lobby.
Updates

We are thinking instead of 'Just Follow the Signs,We would like to try:'Looking for us?' (Large Text)'Follow the Signs (much smaller Text)Also, it is very useful to see the proposed sign dropped on to the photo of the car park pillars I included.Many thanks Added Friday, June 16, 2017

Target Market(s)

Customers, coming for the 1st time, trying to navigate the Underground CarPark towards the appropriate Lift lobby

Industry/Entity Type

Veterinary

Font styles to use
Serif

Colors
f78f20
00a990
0455a3

Requirements
Must have
• Logo.
• Bright. Clear. Not too cluttered.
• Warmth. Humour. Approachable.
• Please include: Building 4, Mezzanine Level
Nice to have
• Please look at our FB pages and Instagram page @7k3rvetclinic for a good feel of who we are.
• Some level of style or image continuity with the Pet Tips Poster (see attached file)
Should not have
• Not have a medical feel

```html
<!DOCTYPE html>
<html lang="en">
<head>
<meta charset="utf-8">
<title>7K3R Vet Clinic – Car Park Sign</title>
<link rel="stylesheet" href="https://fonts.googleapis.com/css2?family=Oswald:wght@500&family=Playfair+Display:wght@400;500&display=swap">
<style>
  :root {
    --orange: #d4872b;
    --teal: #00a98f;
    --blue: #0455a3;
    --slate: #3b6f80;
    --white: #ffffff;
  }
  html, body {
    margin: 0;
    padding: 0;
    overflow: hidden;
    background: var(--white);
  }
  .sign {
    position: relative;
    width: 848px;
    height: 1200px;
    overflow: hidden;
    background: var(--white);
  }
  .brand {
    position: absolute;
    left: 0;
    top: 250px;
    width: 848px;
    display: flex;
    align-items: center;
    justify-content: center;
    gap: 22px;
  }
  .brand-dot {
    width: 44px;
    height: 44px;
    border-radius: 50%;
    background: var(--slate);
  }
  .brand-name {
    font-family: "Playfair Display", serif;
    font-weight: 500;
    font-size: 82px;
    color: var(--slate);
    margin: 0;
    line-height: 1;
  }
  .location {
    position: absolute;
    left: 0;
    top: 508px;
    width: 848px;
    margin: 0;
    text-align: center;
    font-family: "Oswald", sans-serif;
    font-weight: 500;
    font-size: 36px;
    letter-spacing: 0.5px;
    color: var(--orange);
    text-transform: uppercase;
  }
  .headline {
    position: absolute;
    left: 0;
    top: 592px;
    width: 848px;
    margin: 0;
    text-align: center;
    font-family: "Playfair Display", serif;
    font-weight: 500;
    font-size: 70px;
    line-height: 1;
    color: var(--blue);
  }
  .subline {
    position: absolute;
    left: 0;
    top: 695px;
    width: 848px;
    margin: 0;
    text-align: center;
    font-family: "Playfair Display", serif;
    font-weight: 400;
    font-size: 40px;
    line-height: 1;
    color: var(--teal);
  }
  .direction-band {
    position: absolute;
    left: 0;
    top: 800px;
    width: 848px;
    height: 290px;
    background: linear-gradient(90deg, var(--teal) 0 424px, var(--orange) 424px 100%);
  }
  .direction-sign {
    position: absolute;
    left: 279px;
    top: 800px;
    width: 290px;
    height: 290px;
  }
</style>
</head>
<body>
  <main class="sign">
    <div class="brand">
      <span class="brand-dot"></span>
      <h1 class="brand-name">7K3R Vet Clinic</h1>
    </div>

    <p class="location">Building 4, Mezzanine Level</p>

    <h2 class="headline">Looking for us?</h2>
    <p class="subline">Follow the signs</p>

    <div class="direction-band"></div>
    <svg class="direction-sign" viewBox="-150 -150 300 300" role="img" aria-label="Turn left">
      <circle cx="0" cy="0" r="146" fill="var(--blue)" stroke="var(--white)" stroke-width="3"/>
      <circle cx="0" cy="0" r="140" fill="none" stroke="var(--blue)" stroke-width="1"/>
      <polygon fill="var(--white)"
        points="-120,-47 -50,-100 -50,-62 67,-62 67,110 35,110 35,-30 -50,-30 -50,6"/>
    </svg>
  </main>
</body>
</html>
```